Civil Engineering Web design

.Net Web design for a civil engineering company to include a blog page, I will like a site similar to this http://www.layoutgrove.example/demo/58273.html

company name: Dorvil Associates

-Civil/Structural Engineering Solutions

-Engineering Design Development and Consultancy

More Information about the internal pages or links:
1. Each one of the menu choices will take you to a page for that option where I will be able to insert text 2. Our team likewise should be a page with space for a photo of the staff and text space for inserting employee name and title, qualifications and job description and work experience...
Can we have 3 groups for these
Management Staff
Support Staff
Other Staff

3. The blog is a generic blog page where users can add comments to a any subjects raised by our team and submit... When they submit, the comments should be emailed to us 4. Contact us is also a tool for emailing us by users, whereby they provide their email, subject and email body 5. projects is a page that allows insertion of title, one photo and description of the project...
6. services is a page with links on the left for Construction Supervision Civil and Structured Engineering Designs Corporate Recognition

Each on when clicked should display the relevant information for the link which is a gallery of two photos side by side and one description per pair...

Industry/Entity Type

Construction

Requirements
Must have
• User ability to manage content; not design

Pages:
Home
Services
Projects (sub page picture gallery)
Reference
Our Team
Blog
Contact Us

```html
<!DOCTYPE html>
<html lang="en">
<head>
<meta charset="utf-8">
<title>Ravo — Civil Engineering &amp; Services</title>
<link rel="stylesheet" href="https://fonts.googleapis.com/css2?family=Questrial&family=Montserrat:wght@500&family=Open+Sans:wght@400;600&display=swap">
<style>
  :root {
    --yellow: #f8b80a;
    --ink: #1b1b1b;
    --heading-dark: #2a2a2a;
    --text: #555555;
    --text-strong: #3c3c3c;
    --white: #ffffff;
    --footer-bg: #000000;
    --logo-bg: rgba(40, 40, 40, 0.88);
    --dot: #3a3a3a;
  }
  * { box-sizing: border-box; margin: 0; padding: 0; }
  html, body { width: 1199px; height: 1200px; overflow: hidden; background: var(--white); }
  body { position: relative; font-family: "Open Sans", Arial, sans-serif; color: var(--text); }

  .hero { position: absolute; left: 0; top: 0; width: 1199px; height: 722px; overflow: hidden; }
  .hero-photo {
    position: absolute; inset: 0;
    background:
      radial-gradient(ellipse 30% 45% at 55% 45%, rgba(255,255,255,0.75), transparent 70%),
      radial-gradient(ellipse 40% 30% at 60% 10%, rgba(230,160,40,0.55), transparent 70%),
      linear-gradient(180deg, #b9b2a4 0%, #d8d2c6 40%, #cfc6b6 70%, #bdb3a2 100%);
  }

  .brand {
    position: absolute; left: 0; top: 0; width: 357px; height: 143px;
    background: var(--logo-bg);
  }
  .brand-name {
    position: absolute; left: 104px; top: 26px;
    font-family: "Questrial", Arial, sans-serif; font-size: 62px; line-height: 1;
    color: var(--white); letter-spacing: 1px;
  }
  .brand-slogan {
    position: absolute; left: 160px; top: 93px;
    font-family: "Open Sans", Arial, sans-serif; font-size: 14px; color: #bdbdbd;
  }

  .main-nav { position: absolute; left: 0; top: 206px; }
  .nav-active-band { position: absolute; left: 82px; top: 0; }
  .main-nav ul { list-style: none; position: absolute; left: 126px; top: 7px; width: 260px; }
  .main-nav li {
    font-family: "Montserrat", Arial, sans-serif; font-weight: 500; font-size: 23px;
    line-height: 38.5px; color: var(--ink); text-transform: uppercase; white-space: nowrap;
  }
  .main-nav li.is-active { color: var(--white); }

  .hero-caption { position: absolute; left: 483px; top: 358px; }
  .hero-title {
    font-family: "Questrial", Arial, sans-serif; font-size: 45px; font-weight: 400;
    color: var(--ink); letter-spacing: -0.5px; white-space: nowrap;
  }
  .hero-subtitle {
    margin-top: 2px; font-family: "Questrial", Arial, sans-serif; font-size: 26px;
    color: #5a5a5a; white-space: nowrap;
  }

  .slider-dots { position: absolute; left: 561px; top: 685px; display: flex; gap: 4px; }
  .slider-dots span { width: 16px; height: 16px; border-radius: 50%; background: var(--dot); }
  .slider-dots span.is-current { background: var(--yellow); }

  .highlights { position: absolute; top: 764px; left: 0; width: 1199px; }
  .column { position: absolute; top: 0; width: 330px; }
  .column h2 {
    font-family: "Questrial", Arial, sans-serif; font-weight: 400; font-size: 27px;
    color: var(--yellow); text-transform: uppercase; line-height: 1; margin-bottom: 11px;
  }
  .column h2.dark { color: var(--heading-dark); }
  .thumb { width: 317px; height: 154px; }
  .thumb-about { background: linear-gradient(120deg, #2f6fc4 0%, #6f9ad0 45%, #a58a5a 70%, #e0b720 100%); }
  .thumb-project { background: linear-gradient(120deg, #8a9bab 0%, #d6d9de 45%, #c4a878 75%, #a08866 100%); }
  .column h3 {
    font-family: "Open Sans", Arial, sans-serif; font-weight: 400; font-size: 15.5px;
    color: var(--text-strong); margin: 12px 0 4px 2px;
  }
  .column p { font-size: 12px; line-height: 22px; color: var(--text); margin-left: 2px; }

  .blog-post { margin-top: 0; }
  .blog-post + .blog-post { margin-top: 19px; }
  .blog-post h3 { font-weight: 600; font-size: 14.5px; margin: 0 0 2px 3px; }
  .blog-post p { margin-left: 3px; }

  .site-footer {
    position: absolute; left: 0; top: 1117px; width: 1199px; height: 83px;
    background: var(--footer-bg);
  }
  .copyright {
    position: absolute; left: 85px; top: 30px; font-size: 13.5px; color: #d8d8d8;
  }
  .social { position: absolute; left: 1017px; top: 27px; display: flex; gap: 8px; }
  .social span { width: 26px; height: 26px; border-radius: 50%; background: var(--white); }
</style>
</head>
<body>

<header class="hero">
  <div class="hero-photo" role="img" aria-label="Photo of smiling construction workers in hard hats on a building site with excavators behind them"></div>

  <div class="brand">
    <div class="brand-name">Ravo</div>
    <div class="brand-slogan">Slogan goes here</div>
  </div>

  <nav class="main-nav">
    <svg class="nav-active-band" width="280" height="50" viewBox="0 0 280 50" aria-hidden="true">
      <polygon points="0,0 278,0 252,50 0,50" fill="var(--yellow)"/>
      <polyline points="32,19 36,25 32,31" fill="none" stroke="#fff" stroke-width="2.2"/>
    </svg>
    <ul>
      <li class="is-active">Home</li>
      <li>Services</li>
      <li>Projects</li>
      <li>Reference</li>
      <li>Our Team</li>
      <li>Blog</li>
      <li>Contact Us</li>
    </ul>
  </nav>

  <div class="hero-caption">
    <h1 class="hero-title">CIVIL ENGINEERING &amp; SERVICES</h1>
    <p class="hero-subtitle">FUSCE TELLUS SED METUS AUGUE CONVALLIS</p>
  </div>

  <div class="slider-dots">
    <span class="is-current"></span><span></span><span></span><span></span>
  </div>
</header>

<main class="highlights">
  <section class="column" style="left:84px;">
    <h2>About Company</h2>
    <div class="thumb thumb-about" role="img" aria-label="Photo of a worker in a yellow hard hat at a construction site under a blue sky"></div>
    <h3>Ut ante enim dapibus malesuada</h3>
    <p>fringilla eu condimentum quis tellus Aenean porttitor<br>eros vel dolor Donec convallis pede venenatis</p>
  </section>

  <section class="column" style="left:434px;">
    <h2>Recent Projects</h2>
    <div class="thumb thumb-project" role="img" aria-label="Photo of a builder in a hard hat laying paving in front of a new building"></div>
    <h3>Duis quam Nam eget lacus</h3>
    <p>fringilla eu condimentum quis tellus Aenean porttitor<br>eros vel dolor Donec convallis pede ven</p>
  </section>

  <section class="column" style="left:796px; width:340px;">
    <h2 class="dark">Recent Blog</h2>
    <article class="blog-post">
      <h3>Pellentesque faucibus accumsan</h3>
      <p>Sltricies elit Maecenas at justo id velit placerat molestie<br>Donec dictum lectus non odio Cras a ante</p>
    </article>
    <article class="blog-post">
      <h3>Vestibulum ligula augue</h3>
      <p>Altricies elit Maecenas at justo id velit placerat molestie<br>Donec dictum lectus non odio</p>
    </article>
    <article class="blog-post">
      <h3>Etiam est nunc venenatis</h3>
      <p>ultricies elit Maecenas at justo id velit placerat molestie<br>Donec dictum lectus non odio Cras a ante vitae enim</p>
    </article>
  </section>
</main>

<footer class="site-footer">
  <p class="copyright">© 2014 Company Name&nbsp; All right reserved&nbsp; Term of Use</p>
  <div class="social" aria-label="Social links">
    <span></span><span></span><span></span>
  </div>
</footer>

</body>
</html>
```